Brochure Design

Looking for designer to make a brochure (2 sided) similar to attached pdf. Will provide the details and graphics needed. PDF is similar style to what we want. PPT has new content.

```html
<!DOCTYPE html>
<html lang="en">
<head>
<meta charset="utf-8">
<title>LinguaTrace Brochure</title>
<link rel="stylesheet" href="https://fonts.googleapis.com/css2?family=Montserrat:wght@300;400;500;600;700;800;900&family=Quicksand:wght@400;500&display=swap">
<style>
:root{
  --canvas:#e4e5e7;
  --paper:#ffffff;
  --ink-dark:#3b3b3b;
  --panel:#4b4b4b;
  --yellow:#e7e31f;
  --white:#ffffff;
  --text-light:#f1f1f1;
  --steel:#9fb2c6;
  --red:#e3202e;
  --gold:#e6c91f;
  --blue:#4a5bc6;
  --ink:#222222;
}
*{margin:0;padding:0;box-sizing:border-box}
html,body{width:1200px;height:3012px;overflow:hidden}
body{background:var(--canvas);position:relative;font-family:'Montserrat',sans-serif;color:var(--text-light)}
.page{position:absolute;left:49px;width:1101px;background:var(--paper);overflow:hidden;box-shadow:4px 6px 12px rgba(0,0,0,.18)}
.page-front{top:56px;height:1425px}
.page-back{top:1532px;height:1422px}
.abs{position:absolute}

/* front */
.front-bg{left:0;top:37px;width:1101px;height:1388px;background:var(--ink-dark)}
.front-deco{left:0;top:0}
.hero-title{left:74px;top:92px;font-weight:900;font-size:53px;line-height:49px;color:var(--white);letter-spacing:.5px}
.hero-sub{left:74px;top:264px;width:430px;font-family:'Quicksand','Montserrat',sans-serif;font-weight:400;font-size:36px;line-height:34px;color:var(--yellow)}
.intro{left:74px;top:429px;width:800px;font-weight:400;font-size:17.5px;line-height:23.4px}
.intro p{margin-bottom:23.4px}
.compare-title{left:0;width:1101px;top:740px;text-align:center;font-weight:800;font-size:36px;color:var(--yellow)}
.compare-box{left:71px;top:812px;width:958px;height:234px;background:var(--steel);border-radius:18px}
.tool-name{left:18px;top:18px;display:flex;align-items:center;gap:10px}
.tool-square{width:36px;height:36px;background:#4c6fc0;border-radius:4px}
.tool-label{font-size:18px;font-weight:500;line-height:20px;color:#5b6370}
.literal{left:18px;top:88px;width:680px;height:132px;background:var(--white);border-radius:10px;padding:12px 20px;font-size:15.6px;line-height:20px;color:var(--ink)}
.literal .r{color:var(--red)}
.literal .y{color:var(--gold)}
.literal .b{color:var(--blue)}
.legend{left:740px;top:22px;width:210px;font-size:16px;line-height:19.5px;font-weight:500}
.legend div{position:absolute;left:0;width:210px}
.legend .r{color:var(--red)}
.legend .b{color:var(--blue)}
.legend .y{color:var(--gold)}
.plain-box{left:71px;top:1070px;width:958px;height:191px;background:var(--panel);border-radius:18px;text-align:center}
.plain-box h3{margin-top:16px;font-weight:800;font-size:37px;color:var(--white)}
.plain-box p{margin:10px auto 0;width:870px;font-size:16.8px;line-height:21.6px;color:#e8e8e8}
.brand{display:flex;align-items:center}
.brand-dot{width:70px;height:70px;border-radius:50%;background:var(--ink-dark)}
.brand-rule{width:2px;height:80px;background:var(--ink-dark);margin:0 10px}
.brand-name{font-weight:700;font-size:37px;line-height:40px;color:var(--ink-dark)}
.brand-tag{font-weight:600;font-size:12.5px;letter-spacing:1.5px;color:var(--ink-dark);margin-left:8px}
.brand-front{left:752px;top:1313px}
.brand-back{left:64px;top:1310px}

/* back */
.back-bg{left:0;top:35px;width:1101px;height:1235px;background:var(--ink-dark)}
.back-head{left:0;top:35px;width:1068px;height:205px;background:#4f4f4f;border-radius:0 30px 30px 0}
.back-title{left:0;top:70px;width:1068px;text-align:center;font-weight:800;font-size:37px;color:var(--white)}
.back-sub{left:64px;top:128px;width:976px;font-family:'Quicksand','Montserrat',sans-serif;font-size:23px;line-height:23.5px;color:var(--yellow);text-align:justify;text-align-last:center}
.col{top:265px;font-size:16.6px;line-height:21.4px;text-align:justify}
.col-left{left:64px;width:471px}
.col-right{left:569px;width:469px}
.col h2{font-family:'Quicksand','Montserrat',sans-serif;font-weight:400;font-size:37px;line-height:35px;color:var(--yellow);text-align:left;margin-bottom:10px}
.col h4{font-weight:700;font-size:17px;line-height:21.4px;color:var(--white)}
.col ul{list-style:none}
.col li{position:relative;padding-left:36px}
.col-left li::before{content:"•";position:absolute;left:6px;top:0}
.col-right li::before{content:"◦";position:absolute;left:6px;top:0}
.col b{font-weight:700}
.gap{height:21.4px}
.closing{left:569px;top:1062px;width:469px;height:325px;background:var(--panel);border-radius:30px;padding:58px 28px 0;text-align:center;font-family:'Quicksand','Montserrat',sans-serif;font-size:24px;line-height:25px;color:var(--yellow)}
</style>
</head>
<body>

<section class="page page-front">
  <div class="abs front-bg"></div>
  <svg class="abs front-deco" width="1101" height="1425" viewBox="0 0 1101 1425">
    <defs>
      <linearGradient id="photoTone" x1="0" y1="0" x2="0" y2="1">
        <stop offset="0" stop-color="#b9bcc3"/>
        <stop offset=".5" stop-color="#8a8f95"/>
        <stop offset="1" stop-color="#2c3a6e"/>
      </linearGradient>
    </defs>
    <circle cx="898" cy="225" r="194" fill="#4a4a4a"/>
    <circle cx="898" cy="225" r="186" fill="url(#photoTone)" role="img" aria-label="Photo of a lighthouse by the sea with a dark blue car parked in front"/>
    <polygon points="594,1425 732,1269 1101,1269 1101,1425" fill="var(--paper)"/>
  </svg>

  <h1 class="abs hero-title">LinguaTrace:<br>Decode the Real<br>Message</h1>
  <div class="abs hero-sub">No More Robotic Translations—Get Down and Dirty with Real Language</div>

  <div class="abs intro">
    <p>Forget stiff, textbook translations. Our AI-powered<br>system translates slang, typos, emojis, abbreviations,<br>local dialects, and hidden meanings—so nothing gets lost<br>in translation.</p>
    <p>Whether it’s text messages, recorded calls, social media posts,<br>or street slang, LinguaTrace analyzes language like real people use<br>it—raw, unfiltered, and full of nuance. We work across 78+ languages,<br>ensuring you don’t just get the words—you get the real intent behind them.</p>
    <p>Because in an investigation, understanding the truth can mean the difference between<br>a lead and a dead end.</p>
  </div>

  <h2 class="abs compare-title">LinguaTrace vs Online Translator</h2>

  <div class="abs compare-box">
    <div class="abs tool-name">
      <div class="tool-square"></div>
      <div class="tool-label">QuickTranslate</div>
    </div>
    <div class="abs literal">What the hell, <span class="y">steel?</span> I have the package in the <span class="r">refrigerator, very cold and without any bumps</span>. This <span class="r">is neither</span> <span class="y">fula</span> nor junk, it is pure poison for the <span class="r">fine tigers</span>. If you’re up for the game, let me know before <span class="r">they suck it up</span>. But you know, no <span class="b">nonsense</span>, <span class="y">that the chalk is hot</span> and the <span class="y">guanajos</span> are on the prowl. You fall with the <span class="y">guara</span> and we make a clean <span class="r">bisne</span>, <span class="r">shall we?</span></div>
    <svg class="abs" style="left:0;top:0" width="958" height="234" viewBox="0 0 958 234">
      <g stroke="#6b7888" stroke-width="1.5" fill="none">
        <path d="M720 33 H728 V200 H720"/>
        <line x1="728" y1="70" x2="720" y2="70"/>
        <line x1="728" y1="125" x2="720" y2="125"/>
        <line x1="676" y1="173" x2="728" y2="173"/>
      </g>
      <circle cx="676" cy="173" r="5" fill="#6b7888"/>
    </svg>
    <div class="abs legend">
      <div class="r" style="top:0">Too Literal</div>
      <div class="r" style="top:38px">Lack of Understanding<br>Dialect</div>
      <div class="b" style="top:93px">Bad Language /NSFW<br>Topics Often Ignored<br>/Misunderstood</div>
      <div class="y" style="top:177px">Current Slang</div>
    </div>
  </div>

  <div class="abs plain-box">
    <h3>LinguaTrace</h3>
    <p>What’s up, dude? I got the package in the fridge, real cold and no bumps. This ain’t no fake or junk, it’s pure poison for the high rollers. If you’re up for the game, let me know before the swipe it. But you know, no bullshit, the heat is on and the cops are on the prowl. You come up with the dough and we make the deal clean, alright?</p>
  </div>

  <div class="abs brand brand-front">
    <div class="brand-dot"></div>
    <div class="brand-rule"></div>
    <div>
      <div class="brand-name">Terravia</div>
      <div class="brand-tag">Geospatial Intelligence</div>
    </div>
  </div>
</section>

<section class="page page-back">
  <div class="abs back-bg"></div>
  <div class="abs back-head"></div>
  <h2 class="abs back-title">LinguaTrace: The Future of Translation</h2>
  <p class="abs back-sub">Break Language Barriers with Precision Communicate effortlessly across 78 languages with LinguaTrace. Whether it’s text, audio, or images, our cutting-edge translation technology ensures accuracy, nuance, and cultural relevance like never before.</p>

  <div class="abs col col-left">
    <h2>Why LinguaTrace?</h2>
    <h4>Better Translation with Advanced AI</h4>
    <p>Traditional translation apps like QuickTranslate rely on Neural Machine Translation (NMT) and Statistical Machine Translation (SMT) —often resulting in literal and misleading translations.Example:</p>
    <ul>
      <li>QuickTranslate Interpretation: “That cat just kicked the bucket.” → Assumes a feline physically kicked a bucket.</li>
      <li>LinguaTrace Interpretation: Understands that ‘cat’ is slang for a cool person and ‘kicked the bucket’ means death.</li>
    </ul>
    <p>LinguaTrace is powered by a custom Large Language Model (LLM) designed to grasp context, idioms, and cultural nuances, making translations sound more natural and human-like.</p>
    <div class="gap"></div>
    <h4>Up-to-Date Slang, Dialects &amp; Modern Expressions</h4>
    <ul>
      <li>QuickTranslate: Uses outdated language models, often derived from World Assembly transcripts from the 1990s, missing modern slang and dialects.</li>
      <li>GenChat: While advanced, its model updates are over 6 months old, missing real-time language shifts from social media trends.</li>
      <li>LinguaTrace: Slang and dialect updates in near real-time. If a new term trends on ClipFeed today, LinguaTrace incorporates it by the next morning. LinguaTrace is constantly evolving, making it the perfect tool for law enforcement, undercover investigations, and intelligence agencies who need to stay ahead of linguistic shifts.</li>
    </ul>
    <div class="gap"></div>
    <h4>Understands Sensitive Topics</h4>
    <p>Unlike other translation platforms, LinguaTrace provides an accurate, unfiltered understanding of language—even in sensitive or restricted discussions.</p>
    <ul>
      <li>QuickTranslate: Often misunderstands slang, censors words, or provides inaccurate translations.</li>
      <li>GenChat: Prohibits discussion of sex, drugs, and violence.</li>
      <li>LinguaTrace: Custom LLM is trained to understand and translate sex, drug, and violence-related conversations with accuracy and context.</li>
    </ul>
  </div>

  <div class="abs col col-right">
    <h2>Customizable<br>Communication Styles</h2>
    <p style="margin-top:22px">LinguaTrace goes beyond just translating words—it helps you blend in seamlessly by providing multiple conversational styles to match different scenarios. Whether you need to sound like a teenager, a business executive, or someone in a hurry, LinguaTrace adapts accordingly.</p>
    <ul>
      <li><b>Teenager Mode</b> – Uses emojis, slang, and abbreviations to sound authentic to younger generations. (“Yo fr, that’s wild!”)</li>
      <li><b>Professional Mode</b> – Provides a polished, formal tone for business communications. (“Thank you for your patience. We will review your request shortly.”)</li>
      <li><b>Fast &amp; Direct Mode</b> – Short, to-the-point translations for quick interactions. (“Need info now. Meet in 10.”)</li>
      <li><b>Undercover Mode</b> – Designed for intelligence professionals and law enforcement to mimic local dialects, gang slang, and criminal jargon, crucial for narcotics, sex trafficking, and organized crime investigations.</li>
    </ul>
    <h2 style="margin-top:18px;margin-bottom:20px">Privacy &amp; Security First</h2>
    <p>LinguaTrace is built for organizations and individuals who prioritize data security and confidentiality.</p>
    <ul>
      <li>No Third-Party Data Sharing.</li>
      <li>No Auditing or Saving of Text, Images, or Audio</li>
      <li>Can Be Hosted on Classified Networks</li>
      <li>Compatible with Air-Gapped Systems</li>
    </ul>
    <p>(Note: slang updates will be delayed by a month)</p>
  </div>

  <div class="abs closing">LinguaTrace: Beyond Translation<br>True Communication Whether you’re a global business, intelligence agency, or an individual needing true-to-life translations, LinguaTrace is the next-generation language solution you can trust.<br>Experience the future of translation today.</div>

  <div class="abs brand brand-back">
    <div class="brand-dot"></div>
    <div class="brand-rule"></div>
    <div>
      <div class="brand-name">Terravia</div>
      <div class="brand-tag">Geospatial Intelligence</div>
    </div>
  </div>
</section>

</body>
</html>
```